MARGOT ELODIE - brand producing beautiful ladies bags to go through the day in an organized way

We need for a brand in-creation a lifestyle luxury website (ie Renard Castel, Halvick, LuneVera) with an online shop. The brand name will be www.margotelodie.example. Ideally, we would like to host the web in HostNimbus. However, we need specific fonts - Didot (brand name) combined with Century Gothic (for the rest) or perhaps propose a better combination if you feel. The web should contain an e-shop. We would like to have a mobile version of the web too.

Target Market(s)

female customers aged 14 - 35

Industry/Entity Type

Fashion

Contact Information for Business Card

Margot Elodie Travan - CEO; Margot.Travan@margotelodie.example; +420 608 192836
Pavel Travan; Pavel.Travan@margotelodie.example; cell +420 609587214
www.Margotelodie.example

Coding

Coded - Design and coding required

Number of Pages Required

5+ page

Font styles to use
Other font styles liked:
• Didot & Century Gothic or similar

Colors

Designer to choose colors to be used in the design.

Requirements
Must have
• the top line bar - please take inspiration from Halvick (no white background). The background should be incorporated in the main image. The brand name will be home button in top left corner. The brand should have feel of lifestyle luxury but functionality - those should be the features of the products (bags). The bags are currently being designed. Functional e-shop - would like to ideally use hostnimbus.example.
Nice to have
• Personal Information should be hidden.

```html
<!DOCTYPE html>
<html lang="en">
<head>
<meta charset="UTF-8">
<title>Margot Elodie</title>
<link href="https://fonts.googleapis.com/css2?family=Bodoni+Moda:wght@400;500&family=Libre+Baskerville:wght@400&family=Mulish:wght@400;500&display=swap" rel="stylesheet">
<style>
:root{
  --ink:#2b2628;
  --muted:#6a6466;
  --wine:#4a0510;
  --wine-deep:#3c040c;
  --accent:#8a1a24;
  --mist:#f4f2f3;
  --white:#ffffff;
  --line:#d8d4d5;
}
*{margin:0;padding:0;box-sizing:border-box}
html,body{width:1200px;height:3103px;overflow:hidden}
body{position:relative;background:var(--white);color:var(--ink);font-family:"Mulish",sans-serif}
.abs{position:absolute}
.serif{font-family:"Libre Baskerville",serif}

/* header + hero */
.hero{left:0;top:0;width:1200px;height:600px;background:var(--mist)}
.hero-photo{left:660px;top:60px;width:540px;height:540px;
  background:radial-gradient(ellipse 62% 72% at 60% 58%,#7a1a22 0%,#5a0f17 55%,rgba(63,10,16,.6) 80%,rgba(244,242,243,0) 100%)}
.brand{left:149px;top:22px;font-family:"Bodoni Moda",serif;font-size:24px;letter-spacing:1.5px;color:var(--ink)}
.nav a{position:absolute;top:27px;font-size:14px;color:var(--ink);text-decoration:none;letter-spacing:.3px}
.icons svg{position:absolute;top:21px}
.cart-badge{left:1035px;top:10px;width:15px;height:15px;border-radius:50%;background:var(--wine);color:#fff;font-size:10px;line-height:15px;text-align:center}
.hero-title{left:149px;top:196px;font-size:37px;line-height:41px;letter-spacing:.3px;color:var(--ink);z-index:2;white-space:nowrap}
.hero-text{left:149px;top:292px;width:450px;font-size:22.5px;line-height:34px;color:var(--muted);z-index:2}
.btn-explore{left:149px;top:419px;width:195px;height:45px;background:var(--wine);color:#fff;font-size:13px;line-height:45px;text-align:center;letter-spacing:.2px;z-index:2}

/* categories */
.tile-gift{left:149px;top:718px;width:432px;height:600px;background:linear-gradient(150deg,#e6e4e5 0%,#c8262a 40%,#a3151b 70%,#e2dfe0 100%)}
.tile-featured{left:618px;top:675px;width:430px;height:300px;background:linear-gradient(160deg,#b5b4b7,#a4a3a6)}
.tile-new{left:618px;top:1060px;width:433px;height:300px;background:linear-gradient(160deg,#b5b4b7,#a4a3a6)}
.tile-label{font-size:25px;letter-spacing:.6px;color:var(--ink)}

/* recommendations */
.recs{left:0;top:1486px;width:1200px;height:1108px;background:var(--mist)}
.recs-title{left:0;top:1553px;width:1200px;text-align:center;font-size:25px;letter-spacing:.5px}
.card{width:288px;height:440px;background:var(--white);box-shadow:0 1px 4px rgba(0,0,0,.06)}
.card .photo{position:absolute;left:0;top:28px;width:100%;height:270px}
.photo-red{background:radial-gradient(ellipse at 50% 55%,#e0474d 0%,#e85a5f 40%,#ffffff 72%)}
.photo-duo{background:radial-gradient(ellipse at 50% 55%,#d33a42 0%,#dcdcdc 45%,#ffffff 75%)}
.photo-white{background:radial-gradient(ellipse at 50% 55%,#e4e2df 0%,#eeedeb 40%,#ffffff 72%)}
.card .name{position:absolute;left:28px;top:318px;font-family:"Libre Baskerville",serif;font-size:16px;letter-spacing:.4px;color:var(--ink)}
.card .desc{position:absolute;left:28px;top:345px;width:240px;font-size:12px;line-height:18px;color:var(--muted)}
.card .shop{position:absolute;left:28px;top:391px;font-size:12.5px;color:var(--accent);letter-spacing:.2px}
.card .shop svg{vertical-align:-1px;margin-left:8px}

/* newsletter */
.newsletter{left:0;top:2594px;width:1200px;height:244px;background:var(--wine)}
.nl-title{left:149px;top:2661px;font-size:25px;color:#fff;letter-spacing:.5px}
.nl-text{left:149px;top:2704px;width:395px;font-size:15.5px;line-height:23px;color:#fff}
.nl-input{left:588px;top:2714px;width:300px;height:45px;background:#fff;border:1px solid var(--line);font-size:12px;font-style:italic;color:#9a9597;padding-left:14px;line-height:43px}
.nl-btn{left:900px;top:2714px;width:149px;height:45px;background:#fff;color:var(--wine);font-size:13px;text-align:center;line-height:45px;letter-spacing:.3px}

/* footer */
.foot-brand{left:149px;top:2892px;font-family:"Mulish",sans-serif;font-size:20px;letter-spacing:1px;color:var(--ink)}
.foot-mark{left:149px;top:2923px;width:16px;height:16px;background:var(--ink)}
.foot-text{left:149px;top:2975px;width:250px;font-size:12.5px;line-height:18px;color:var(--muted)}
.foot-col a{position:absolute;font-size:15.5px;color:var(--ink);text-decoration:none;letter-spacing:.2px}
.copyright{left:0;top:3066px;width:1200px;height:37px;background:var(--mist);text-align:center;font-size:14px;line-height:37px;color:var(--ink);letter-spacing:.3px}
</style>
</head>
<body>

<section class="abs hero"></section>
<div class="abs hero-photo" role="img" aria-label="Hand holding a burgundy croc-embossed leather crossbody bag with a gold clasp"></div>

<header>
  <div class="abs brand">MARGOT ELODIE</div>
  <nav class="nav">
    <a style="left:488px" href="#">WHAT'S NEW</a>
    <a style="left:641px" href="#">GIFTS</a>
    <a style="left:739px" href="#">BAGS</a>
  </nav>
  <div class="icons">
    <svg style="left:930px" width="24" height="24" viewBox="0 0 24 24" fill="none" stroke="#2b2628" stroke-width="1.5"><circle cx="10" cy="10" r="8"/><line x1="16" y1="16" x2="23" y2="23"/></svg>
    <svg style="left:977px" width="22" height="24" viewBox="0 0 22 24" fill="none" stroke="#2b2628" stroke-width="1.5"><circle cx="11" cy="7" r="5.5"/><path d="M1 23c0-6 4.5-9 10-9s10 3 10 9"/></svg>
    <svg style="left:1020px" width="22" height="24" viewBox="0 0 22 24" fill="none" stroke="#2b2628" stroke-width="1.5"><path d="M2 8h18l-1 15H3z"/><path d="M7 8V5a4 4 0 0 1 8 0v3"/></svg>
    <div class="abs cart-badge">1</div>
  </div>
</header>

<h1 class="abs serif hero-title" style="font-weight:400">THE ABSOLUTE PERFECT<br>HOLIDAY GIFT FOR HER</h1>
<p class="abs hero-text">Lorem ipsum dolor sit amet, consectetur adipiscing elit. Donec felis ex, vesti bulum vel mi eget.</p>
<div class="abs btn-explore">EXPLORE SELECTION</div>

<div class="abs tile-gift" role="img" aria-label="Red gift box tied with a satin ribbon bow"></div>
<div class="abs serif tile-label" style="left:149px;top:1345px">GIFTS FOR HER</div>
<div class="abs tile-featured" role="img" aria-label="Blue floral print shoulder bag with chain strap"></div>
<div class="abs serif tile-label" style="left:618px;top:1001px">FEATURED BAGS</div>
<div class="abs tile-new" role="img" aria-label="Collection of small top-handle bags in plum, black, brown and olive"></div>
<div class="abs serif tile-label" style="left:618px;top:1387px">NEW COLLECTION</div>

<section class="abs recs"></section>
<h2 class="abs serif recs-title" style="font-weight:400">TOP RECOMMENDATIONS</h2>

<article class="abs card" style="left:149px;top:1614px"><div class="photo photo-red" role="img" aria-label="Red leather tote bag"></div><div class="name">PRODUCT NAME</div><p class="desc">Lorem ipsum dolor sit amet, consectetur adipiscing elit.</p><div class="shop">SHOP NOW<svg width="6" height="10" viewBox="0 0 6 10" fill="none" stroke="#8a1a24" stroke-width="1.2"><path d="M1 1l4 4-4 4"/></svg></div></article>
<article class="abs card" style="left:457px;top:1614px"><div class="photo photo-duo" role="img" aria-label="Red and silver satchel bag"></div><div class="name">PRODUCT NAME</div><p class="desc">Lorem ipsum dolor sit amet, consectetur adipiscing elit.</p><div class="shop">SHOP NOW<svg width="6" height="10" viewBox="0 0 6 10" fill="none" stroke="#8a1a24" stroke-width="1.2"><path d="M1 1l4 4-4 4"/></svg></div></article>
<article class="abs card" style="left:763px;top:1614px"><div class="photo photo-white" role="img" aria-label="White leather satchel bag with gold clasp"></div><div class="name">PRODUCT NAME</div><p class="desc">Lorem ipsum dolor sit amet, consectetur adipiscing elit.</p><div class="shop">SHOP NOW<svg width="6" height="10" viewBox="0 0 6 10" fill="none" stroke="#8a1a24" stroke-width="1.2"><path d="M1 1l4 4-4 4"/></svg></div></article>

<article class="abs card" style="left:149px;top:2078px"><div class="photo photo-red" role="img" aria-label="Red leather tote bag"></div><div class="name">PRODUCT NAME</div><p class="desc">Lorem ipsum dolor sit amet, consectetur adipiscing elit.</p><div class="shop">SHOP NOW<svg width="6" height="10" viewBox="0 0 6 10" fill="none" stroke="#8a1a24" stroke-width="1.2"><path d="M1 1l4 4-4 4"/></svg></div></article>
<article class="abs card" style="left:457px;top:2078px"><div class="photo photo-duo" role="img" aria-label="Red and silver satchel bag"></div><div class="name">PRODUCT NAME</div><p class="desc">Lorem ipsum dolor sit amet, consectetur adipiscing elit.</p><div class="shop">SHOP NOW<svg width="6" height="10" viewBox="0 0 6 10" fill="none" stroke="#8a1a24" stroke-width="1.2"><path d="M1 1l4 4-4 4"/></svg></div></article>
<article class="abs card" style="left:763px;top:2078px"><div class="photo photo-white" role="img" aria-label="White leather satchel bag with gold clasp"></div><div class="name">PRODUCT NAME</div><p class="desc">Lorem ipsum dolor sit amet, consectetur adipiscing elit.</p><div class="shop">SHOP NOW<svg width="6" height="10" viewBox="0 0 6 10" fill="none" stroke="#8a1a24" stroke-width="1.2"><path d="M1 1l4 4-4 4"/></svg></div></article>

<section class="abs newsletter"></section>
<h3 class="abs serif nl-title" style="font-weight:400">SIGN UP TO OUR NEWSLETTER</h3>
<p class="abs nl-text">Integer ut velit ipsum. Sed a lorem purus. Mauris dolor nunc, viverra eu lorem sit amet, mattis lacinia ex. Donec bibendum ante metus.</p>
<div class="abs nl-input">E-mail Address</div>
<div class="abs nl-btn">SUBSCRIBE</div>

<footer>
  <div class="abs foot-brand">MARGOT ELODIE</div>
  <div class="abs foot-mark"></div>
  <p class="abs foot-text">Pellentesque tincidunt, erat quis convallis mollis, mi nulla accumsan odio, ut scelerisque mi ante euismod ligula.</p>
  <div class="foot-col">
    <a style="left:478px;top:2876px" href="#">ABOUT</a>
    <a style="left:478px;top:2921px" href="#">FAQS</a>
    <a style="left:478px;top:2966px" href="#">CAREERS</a>
    <a style="left:478px;top:3010px" href="#">CONTACT</a>
    <a style="left:675px;top:2876px" href="#">SHIPPING</a>
    <a style="left:675px;top:2921px" href="#">RETURN &amp; REFUNDS</a>
    <a style="left:675px;top:2966px" href="#">PRIVACY POLICY</a>
    <a style="left:675px;top:3010px" href="#">TERMS &amp; CONDITIONS</a>
    <a style="left:959px;top:2875px" href="#">FRIENDLOOP</a>
    <a style="left:959px;top:2920px" href="#">SNAPGRID</a>
    <a style="left:959px;top:2965px" href="#">CHIRPLINE</a>
  </div>
  <div class="abs copyright">MARGOT ELODIE 2020. ALL RIGHTS RESERVED.</div>
</footer>

</body>
</html>
```